Expanding Software Company Needs a Wordpress Design Project

Our software company is expanding, and we are looking for a fantastic Wordpress designer that we can work with on this small project to start, and ideally develop a relationship with over time. This initial project will require the designer to either identify and customize an existing Wordpress Theme or to create a new WP Theme from scratch.
What we are looking for in a WP Theme needs to be modern, creative, professional, and colorful. The Template also needs to be scalable and able to grow with our business. We have many related businesses primarily in the field of home-repair and we would like to be able to use this same template framework for our other businesses, but be able to change / modify the color scheme and some of the basic features like images, fonts, and navigation buttons titles. Ultimately, we want people to be able to go from one of our websites to another and not feel like it is the same website and cause confusion for the end-user.

Please submit an example home page and inside page for each of the following types of businesses (so we can see how the design can vary from site to site):
- Window Washing
- Painting
- Plumbing
Updates

Project Deadline Extended
Reason: Deadline Extended due to Holiday in the United States. Thank you.

Industry/Entity Type

Software

Requirements
Must have
• 1. We are looking for a standard Five Page design with Spectacular Home Page, About Us, Services, Gallery, and Contact Us pages, though we need to have some flexibility in the main menu/sub-menu options as we grow.
2. Need the ability to modify throughout with different color schemes, fonts, and images.
3. The navigation buttons must be visible on each page, but does not have to be “at the top”…. It can be wherever your design allows….but must be consistent on every page.
4. The Home Landing Page needs to be exciting and attractive to the eye. The other, inside pages can be less so, but still needs to be more than just text.
5. We would like to have testimonial and FAQ pages as optional plugins for scalability.
6. The Contact Us page needs to have a customizable form that could be a simple contact form, or could be for requesting a free-quote.
7. Need the ability to integrate with a newsletter / mailing list.
8. We’ll need links and sharing buttons for social media available as options as well, though do not always want them visible on the site.
9. The site needs to be user friendly and easy to navigate.
Nice to have
• Example: An example of a website/theme we like is: http://brushwellcoatings.example

```html
<!DOCTYPE html>
<html lang="en">
<head>
<meta charset="utf-8">
<title>Brushwell – Painting Company</title>
<link href="https://fonts.googleapis.com/css2?family=Noto+Serif:wght@400;700&family=Open+Sans:wght@400;600;700&display=swap" rel="stylesheet">
<style>
  :root {
    --page-bg: #f1efe6;
    --white: #ffffff;
    --ink: #4a4a4a;
    --ink-soft: #5c5c5c;
    --orange: #ff8c00;
    --orange-footer: #ffa51c;
    --cyan: #00c3d5;
    --green: #a8d300;
    --logo-green: #7cc242;
    --dash: #d6d6d6;
    --submit-top: #ff5a1a;
    --submit-bottom: #e23c0c;
    --serif: "Noto Serif", Georgia, serif;
    --sans: "Open Sans", Arial, sans-serif;
  }
  * { box-sizing: border-box; margin: 0; padding: 0; }
  html, body { width: 941px; height: 1200px; overflow: hidden; }
  body { position: relative; background: var(--page-bg); font-family: var(--sans); color: var(--ink); }
  .abs { position: absolute; }

  .header-band { left: 0; top: 0; width: 941px; height: 362px; background: var(--white); }

  .font-tools { top: 15px; left: 583px; display: flex; align-items: center; gap: 6px; font-size: 10px; color: var(--ink-soft); }
  .font-tools .select { width: 46px; height: 17px; border: 1px solid #cfcfcf; background: var(--white); display: flex; align-items: center; justify-content: space-between; padding: 0 2px 0 10px; margin-right: 10px; font-size: 11px; color: #999; }
  .font-tools .swatch { width: 24px; height: 11px; background: #ffab17; }
  .font-tools .arrow { width: 11px; height: 11px; border: 1px solid #888; font-size: 6px; line-height: 9px; text-align: center; color: #333; }

  .search { left: 655px; top: 76px; width: 193px; height: 20px; border: 1px solid #dcdcdc; background: var(--white); font-size: 7px; color: #aaa; padding: 5px 6px; }
  .search svg { position: absolute; right: 5px; top: 4px; }

  .brand { left: 107px; top: 78px; display: flex; align-items: center; gap: 4px; }
  .brand-dot { width: 36px; height: 36px; border-radius: 50%; background: var(--logo-green); }
  .brand-name { font-family: var(--serif); font-size: 46px; line-height: 1; color: #3a3a3a; }

  .main-nav { left: 437px; top: 108px; display: flex; font-size: 14px; color: var(--ink); }
  .main-nav span.sep { margin: 0 15px; }

  .hero { left: 94px; top: 144px; width: 753px; height: 363px;
    background: linear-gradient(90deg, #cfa276 0%, #d9b690 30%, #e8dccd 55%, #ecebe6 75%, #e4e2dc 100%); }
  .hero-title { left: 26px; top: 150px; font-size: 27px; line-height: 36px; color: var(--white); text-shadow: 0 1px 3px rgba(0,0,0,.35); letter-spacing: .5px; }
  .hero-dots { left: 337px; top: 337px; display: flex; gap: 3px; }
  .hero-dots i { width: 13px; height: 13px; border-radius: 50%; background: #333; border: 1px solid #222; }
  .hero-dots i.on { background: var(--white); border: 2px solid #333; }

  .content-panel { left: 94px; top: 507px; width: 753px; height: 583px; background: var(--white); }

  .welcome-title { left: 94px; top: 527px; width: 753px; text-align: center; font-family: var(--serif); font-size: 17px; color: #444; }
  .dashed { border-top: 1px dashed var(--dash); height: 0; }
  .intro { left: 100px; top: 570px; width: 741px; text-align: center; font-size: 10px; line-height: 15.7px; color: var(--ink-soft); }

  .card { top: 677px; width: 235px; height: 276px; color: var(--white); }
  .card-video { left: 102px; background: var(--cyan); }
  .card-testimonial { left: 353px; background: var(--orange); }
  .card-faq { left: 603px; background: var(--green); }
  .card h2 { position: absolute; left: 17px; top: 16px; font-family: var(--serif); font-weight: 400; font-size: 16px; }
  .card .rule { position: absolute; left: 0; top: 43px; width: 235px; border-top: 1px dashed rgba(255,255,255,.6); }

  .video-thumb { left: 13px; top: 53px; width: 206px; height: 134px; border: 4px solid var(--white);
    background: linear-gradient(135deg, #3fa6d8 0%, #8fc9e6 40%, #d9b26e 70%, #c2822e 100%); }
  .video-thumb svg { position: absolute; left: 78px; top: 44px; }
  .video-text { left: 10px; top: 196px; width: 215px; text-align: center; font-size: 10px; line-height: 16px; }

  .portrait { left: 16px; top: 53px; width: 75px; height: 77px; border: 4px solid var(--white);
    background: linear-gradient(160deg, #8a8f94 0%, #c8a58c 55%, #5a5f66 100%); box-shadow: 0 1px 3px rgba(0,0,0,.25); }
  .person-name { left: 99px; top: 67px; font-size: 13px; font-weight: 600; color: #5a3a10; }
  .person-role { left: 99px; top: 86px; font-size: 10px; font-weight: 700; }
  .person-co { left: 99px; top: 100px; font-size: 8px; font-weight: 700; }
  .quote-mark { font-family: var(--serif); font-size: 22px; font-weight: 700; line-height: 1; }
  .quote-open { left: 7px; top: 143px; }
  .quote-close { left: 216px; top: 208px; }
  .quote-text { left: 14px; top: 154px; width: 210px; text-align: center; font-size: 10px; line-height: 15.7px; }

  .faq-list { left: 19px; top: 59px; width: 205px; list-style: none; font-size: 10px; line-height: 15.5px; }
  .faq-list li { position: relative; padding-left: 16px; margin-bottom: 12.5px; }
  .faq-list li::before { content: ""; position: absolute; left: 0; top: 5px; width: 7px; height: 7px; border-radius: 50%; background: var(--white); }

  .card-link { top: 263px; left: 48px; width: 140px; height: 24px; background: var(--white);
    border-radius: 40% 55% 45% 60% / 60% 45% 55% 40%; box-shadow: 0 3px 4px rgba(0,0,0,.08);
    text-align: center; font-size: 10px; line-height: 24px; }
  .card-video .card-link { color: var(--cyan); }
  .card-testimonial .card-link { color: var(--orange); }
  .card-faq .card-link { color: #8cb300; }

  .newsletter-label { left: 166px; top: 1036px; font-family: var(--serif); font-size: 16px; color: #444; }
  .newsletter-input { left: 336px; top: 1033px; width: 342px; height: 33px; background: #f0f0f0; border: 1px solid #ddd; font-size: 10px; color: #666; padding: 9px 13px; }
  .newsletter-submit { left: 678px; top: 1033px; width: 92px; height: 33px; background: linear-gradient(var(--submit-top), var(--submit-bottom)); color: var(--white); font-weight: 700; font-size: 12px; text-align: center; line-height: 33px; }

  .footer { left: 0; top: 1111px; width: 941px; height: 89px; background: var(--orange-footer); color: var(--white); }
  .footer-nav { left: 101px; top: 22px; font-size: 10px; display: flex; }
  .footer-nav .sep { margin: 0 11px; }
  .copyright { left: 101px; top: 42px; font-size: 10px; }
  .social { left: 739px; top: 26px; display: flex; gap: 8px; }
  .social i { width: 28px; height: 28px; border-radius: 50%; background: var(--white); }
</style>
</head>
<body>
  <div class="abs header-band"></div>

  <div class="abs font-tools">
    <span>Font Size</span>
    <span class="select">A<sup>+</sup><span class="arrow">▼</span></span>
    <span>Font Size</span>
    <span class="select"><span class="swatch"></span><span class="arrow">▼</span></span>
  </div>

  <div class="abs search">Type search
    <svg width="11" height="11" viewBox="0 0 11 11"><circle cx="4.5" cy="4.5" r="3.3" fill="none" stroke="#999" stroke-width="1.2"/><line x1="7" y1="7" x2="10" y2="10" stroke="#999" stroke-width="1.4"/></svg>
  </div>

  <div class="abs brand">
    <span class="brand-dot"></span>
    <span class="brand-name">Brushwell</span>
  </div>

  <nav class="abs main-nav">
    <span>Home</span><span class="sep">|</span>
    <span>About Us</span><span class="sep">|</span>
    <span>Services</span><span class="sep">|</span>
    <span>Gallery</span><span class="sep">|</span>
    <span>Contact Us</span>
  </nav>

  <section class="abs hero" role="img" aria-label="Photo of two smiling people painting a wall with paint rollers">
    <h1 class="abs hero-title" style="font-weight:400">We are a painting<br>business Company</h1>
    <div class="abs hero-dots"><i class="on"></i><i></i><i></i><i></i></div>
  </section>

  <div class="abs content-panel"></div>

  <h2 class="abs welcome-title" style="font-weight:400">Welcome to Brushwell</h2>
  <div class="abs dashed" style="left:98px; top:556px; width:749px;"></div>
  <p class="abs intro">Lorem ipsum dolor sit amet, consectetur adipisicing elit, sed do eiusmod tempor incididunt ut labore et dolore magna aliqua. Ut enim ad minim veniam, quis nostrud exercitation ullamco laboris nisi ut aliquip ex ea commodo consequat. Duis aute irure dolor in reprehenderit in voluptate velit esse cillum dolore eu fugiat nulla pariatur. Excepteur sint occaecat cupidatat non proident, sunt in culpa qui officia deserunt mollit anim id est laborum.Sed ut perspiciatis unde omnis iste natus error sit voluptatem accusantium doloremque laudantium, totam rem aperiam, eaque ipsa quae ab illo inventore veritatis et quasi architecto beatae vitae dicta sunt explicabo.</p>

  <section class="abs card card-video">
    <h2>Watch a Video</h2>
    <div class="rule"></div>
    <div class="abs video-thumb" role="img" aria-label="Video still of a bright painted bedroom with a desk and bed">
      <svg width="40" height="44" viewBox="0 0 40 44"><polygon points="4,2 38,22 4,42" fill="rgba(255,255,255,.75)"/></svg>
    </div>
    <p class="abs video-text">Lorem Ipsum is simply dummy text of the printing and typesetting industry.</p>
    <div class="abs card-link">View More</div>
  </section>

  <section class="abs card card-testimonial">
    <h2>Testimonials</h2>
    <div class="rule"></div>
    <div class="abs portrait" role="img" aria-label="Portrait of the client giving the testimonial"></div>
    <div class="abs person-name">Nolan Avery</div>
    <div class="abs person-role">General Manager</div>
    <div class="abs person-co">Hue Works ,Texas</div>
    <span class="abs quote-mark quote-open">“</span>
    <p class="abs quote-text">Sed ut perspiciatis unde omnis iste natus error sit voluptatem accusantium doloremque laudantium, totam rem aperiam, eaque ipsa quae ab illo inventore veritatis et quasi architecto beatae vitae dicta sunt explicabo.</p>
    <span class="abs quote-mark quote-close">”</span>
    <div class="abs card-link">Read More</div>
  </section>

  <section class="abs card card-faq">
    <h2>FAQ’s</h2>
    <div class="rule"></div>
    <ul class="abs faq-list">
      <li>Lorem Ipsum has industry's standard?</li>
      <li>Popular belief, simply?</li>
      <li>Variations of passages of Lorem Ipsum?</li>
      <li>The standard chunk of Lorem Ipsum?</li>
      <li>Lorem ipsum dolor sit amet, consectetur adipisicing?</li>
      <li>Do you sub-contract your projects?</li>
    </ul>
    <div class="abs card-link">Read More</div>
  </section>

  <div class="abs dashed" style="left:98px; top:1006px; width:749px;"></div>

  <h3 class="abs newsletter-label" style="font-weight:400">Sign Up Newsletter</h3>
  <div class="abs newsletter-input">Enter your email address...</div>
  <div class="abs newsletter-submit">SUBMIT</div>

  <footer class="abs footer">
    <nav class="abs footer-nav">
      <span>Home</span><span class="sep">|</span>
      <span>About Us</span><span class="sep">|</span>
      <span>Services</span><span class="sep">|</span>
      <span>Gallery</span><span class="sep">|</span>
      <span>Contact Us</span>
    </nav>
    <div class="abs copyright">Copyright ©2013 Brushwell, All rights reserved</div>
    <div class="abs social" aria-label="Social media links"><i></i><i></i><i></i></div>
  </footer>
</body>
</html>
```